Business Card for Fashion House

We need a business card design for our personalize fashion service for our customers. the business card should reflect reliability, luxury and creativity.
The brand Gravetto is extracted from "Graceful Vetto"; Gravetto provides fashion designs sprinkled with luxury and style tailored for our elite clients character profile.
Gravetto is created for those who embody class and elegance with a passion for style.
Target Market(s)
Affluent Customers
Industry/Entity Type
Fashion
Contact Information for Business Card
Rania Bou Khalil
Fashion Designer
Telephone: +971 5550123
Mobile +971 555987
Emal q@z.com
Website www.gravetto-example.com
Social Media Youtube g+ Facebook Instagram Pin /gravetto
Font styles to use
Other font styles liked:
- Audrey provided
Look and feel
Each slider illustrates characteristics of the customer's brand and the style your logo design should communicate.

```html
<!DOCTYPE html>
<html lang="en">
<head>
<meta charset="utf-8">
<title>Gravetto Business Card</title>
<link rel="stylesheet" href="https://fonts.googleapis.com/css2?family=Open+Sans:wght@300;400&display=swap">
<style>
  :root {
    --page: #e9e6e2;
    --card: #2f2a29;
    --ink: #ffffff;
    --ink-soft: #d9d6d4;
  }
  * { margin: 0; padding: 0; box-sizing: border-box; }
  html, body { width: 1200px; height: 1200px; overflow: hidden; }
  body {
    background: var(--page);
    font-family: "Open Sans", Arial, sans-serif;
    color: var(--ink);
    position: relative;
  }
  .card {
    position: absolute;
    left: 180px;
    width: 840px;
    height: 480px;
    background: var(--card);
    box-shadow: 0 10px 30px rgba(0,0,0,0.18);
  }
  .card--front { top: 90px; }
  .card--back { top: 630px; }

  .brand {
    position: absolute;
    display: flex;
    align-items: center;
    gap: 22px;
  }
  .brand__dot {
    width: 26px; height: 26px;
    border: 3px solid var(--ink);
    border-radius: 50%;
  }
  .brand__name {
    font-weight: 300;
    font-size: 44px;
    letter-spacing: 18px;
    text-transform: uppercase;
    color: var(--ink);
  }
  .card--front .brand { left: 50%; top: 195px; transform: translateX(-50%); }
  .card--back .brand { left: 110px; top: 185px; }

  .social {
    position: absolute;
    display: flex;
    align-items: center;
    gap: 8px;
    font-size: 15px;
    font-weight: 400;
    color: var(--ink-soft);
  }
  .social__mark { width: 12px; height: 12px; background: var(--ink-soft); }
  .card--front .social { right: 190px; top: 290px; }
  .card--back .social { right: 40px; top: 34px; }

  .person { position: absolute; left: 40px; bottom: 40px; }
  .person__name { font-size: 27px; font-weight: 400; line-height: 1.1; }
  .person__role { font-size: 17px; font-weight: 300; color: var(--ink-soft); }

  .contact {
    position: absolute;
    bottom: 40px;
    list-style: none;
    font-size: 15px;
    font-weight: 400;
  }
  .contact li { display: flex; align-items: center; gap: 8px; line-height: 26px; }
  .contact svg { width: 15px; height: 15px; flex: none; }
  .contact--phones { left: 400px; }
  .contact--web { left: 590px; }
</style>
</head>
<body>

<section class="card card--front" aria-label="Card front">
  <div class="brand">
    <span class="brand__dot"></span>
    <span class="brand__name">Gravetto</span>
  </div>
  <div class="social"><span class="social__mark"></span>/gravetto</div>
</section>

<section class="card card--back" aria-label="Card back">
  <div class="social"><span class="social__mark"></span>/gravetto</div>

  <div class="brand">
    <span class="brand__dot"></span>
    <span class="brand__name">Gravetto</span>
  </div>

  <div class="person">
    <p class="person__name">Rania Bou Khalil</p>
    <p class="person__role">Fashion Designer</p>
  </div>

  <ul class="contact contact--phones">
    <li>
      <svg viewBox="0 0 16 16"><path d="M4 1l3 3-2 2c1 2 3 4 5 5l2-2 3 3-2 3C7 14 2 9 1 3z" fill="#fff"/></svg>
      +971 5550123
    </li>
    <li>
      <svg viewBox="0 0 16 16"><rect x="4" y="1" width="8" height="14" rx="1.5" fill="none" stroke="#fff" stroke-width="1.5"/><circle cx="8" cy="12.5" r="1" fill="#fff"/></svg>
      +971 555987
    </li>
  </ul>

  <ul class="contact contact--web">
    <li>
      <svg viewBox="0 0 16 16"><rect x="1" y="3" width="14" height="10" fill="none" stroke="#fff" stroke-width="1.4"/><path d="M1 3l7 6 7-6" fill="none" stroke="#fff" stroke-width="1.4"/></svg>
      q@z.com
    </li>
    <li>
      <svg viewBox="0 0 16 16"><circle cx="8" cy="8" r="6.5" fill="none" stroke="#fff" stroke-width="1.4"/><path d="M1.5 8h13M8 1.5c-3 3.5-3 9.5 0 13M8 1.5c3 3.5 3 9.5 0 13" fill="none" stroke="#fff" stroke-width="1.2"/></svg>
      www.gravetto-example.com
    </li>
  </ul>
</section>

</body>
</html>
```